1 Page for Computer Repair Website

Looking for a 1 page website with a design that compliments the business card and pamphlet that have already been made (attached files). It should look business professional and easy to read. Email and phone number should be somewhere near the top of the website, visible when the page loads. I don't want any forms for people to mess with. No "Contact Us" form or entering in email for newsletter. Customers will just be looking at this site to confirm we are professionals and have our business in order.

Target Market(s)

Home and small business

Industry/Entity Type

Computer Repair

Coding

Coded - Design and coding required

Number of Pages Required

1 page

Font styles to use
Other font styles liked:
• Helvetica variations used in pamphlet and card

Colors
0455a3
cfdeed
85abd2
3276b5
85cae6
ffffff

Requirements
Must have
• Compliment the pamphlet and business card in color choices and font use. Pleasing to the eye and easy to read through categories and text.
Should not have
• Forms. No "enter name and email here" or anything of the sort.

```html
<!DOCTYPE html>
<html lang="en">
<head>
<meta charset="utf-8">
<title>QuickByte Computer Repair</title>
<link rel="stylesheet" href="https://fonts.googleapis.com/css2?family=Open+Sans:wght@400;600;700&display=swap">
<style>
:root{
  --blue:#0455a3;
  --blue-mid:#3276b5;
  --blue-soft:#85abd2;
  --blue-pale:#cfdeed;
  --sky:#85cae6;
  --white:#ffffff;
  --ink:#333a44;
  --dark:#2b2f35;
  --darker:#1f2226;
  --grey:#e9ecef;
}
*{box-sizing:border-box;margin:0;padding:0}
html,body{width:811px;height:1200px;overflow:hidden}
body{font-family:"Open Sans",Arial,sans-serif;background:var(--white);color:var(--ink)}
.page{width:811px;height:1200px;position:relative}

.top-bar{height:75px;position:relative;padding:0 18px}
.top-email{position:absolute;left:18px;top:38px;font-size:13px;color:var(--blue)}
.brand{position:absolute;left:50%;top:14px;transform:translateX(-50%);display:flex;align-items:center;gap:6px}
.brand-name{font-size:22px;font-weight:700;color:var(--blue);letter-spacing:1px}
.brand-dot{width:10px;height:10px;border-radius:50%;background:var(--sky)}
.social{position:absolute;right:18px;top:12px;display:flex;gap:6px}
.social span{width:20px;height:20px;border-radius:50%;background:var(--blue-mid)}
.top-tel{position:absolute;right:18px;top:42px;font-size:13px;color:var(--blue)}

.main-nav{height:22px;background:var(--blue);display:flex;justify-content:center;gap:0}
.main-nav a{color:var(--white);text-decoration:none;font-size:10px;font-weight:600;padding:0 22px;line-height:22px;border-right:1px solid rgba(255,255,255,.35)}
.main-nav a:last-child{border-right:none}

.hero{height:238px;position:relative;background:linear-gradient(180deg,#f2f3f4 0%,#dfe2e5 100%)}
.hero-visual{position:absolute;left:60px;top:10px;width:300px;height:215px;background:radial-gradient(ellipse at 55% 55%,#c4c9ce 0%,#dfe2e5 70%,transparent 100%)}
.hero-tagline{position:absolute;left:425px;top:108px;width:250px;font-size:15px;line-height:1.3;color:var(--blue)}
.hero-arrow{position:absolute;top:106px;width:24px;height:24px;border-radius:50%;background:#3a3f45;display:flex;align-items:center;justify-content:center}
.hero-arrow.prev{left:14px}
.hero-arrow.next{right:14px}

.section-title{text-align:center;font-size:21px;font-weight:700;color:var(--blue);letter-spacing:.5px;padding-top:12px}
.section-title::after{content:"";display:block;width:120px;height:2px;background:var(--blue);margin:4px auto 0}
.about-head{height:43px}
.about-body{height:82px;background:var(--blue);color:var(--white);text-align:center;font-size:13px;font-weight:600;line-height:1.3;padding:10px 90px}

.quote{height:113px;position:relative;background:linear-gradient(90deg,#2e343b 0%,#4d5661 45%,#6b5a48 100%)}
.quote p{position:absolute;left:80px;right:80px;top:24px;color:var(--white);text-align:center;font-size:13.5px;line-height:1.3}
.quote .mark{position:absolute;color:var(--white);font-size:44px;font-family:Georgia,serif;line-height:1}
.quote .open{left:54px;top:14px}
.quote .close{right:54px;top:62px}

.services-head{height:47px}
.services{height:395px;display:grid;grid-template-columns:1fr 1fr;grid-template-rows:repeat(4,1fr);padding:10px 40px 0;column-gap:30px}
.service{display:flex;gap:14px;align-items:flex-start}
.service-icon{flex:0 0 44px;height:44px;border-radius:50%;background:var(--blue-pale);border:2px solid var(--blue-soft)}
.service p{font-size:10.5px;line-height:1.4;color:var(--blue-mid)}

.contact-head{height:55px;background:var(--dark);text-align:center;color:var(--white);font-size:21px;font-weight:700;line-height:55px;margin-top:32px}
.contact-body{height:73px;background:var(--blue);padding:10px 60px;color:var(--white)}
.contact-body div{font-size:18px;line-height:26px}
.site-footer{height:32px;background:var(--darker);color:var(--blue-soft);font-size:8px;text-align:center;line-height:32px}
</style>
</head>
<body>
<div class="page">
  <header class="top-bar">
    <div class="top-email">Email: dan@quickbyte.com</div>
    <div class="brand"><span class="brand-dot"></span><span class="brand-name">QUICKBYTE</span></div>
    <div class="social"><span></span><span></span><span></span><span></span></div>
    <div class="top-tel">TEL: 01234 000 111</div>
  </header>

  <nav class="main-nav">
    <a href="#">HOME</a><a href="#">ABOUT US</a><a href="#">SERVICES</a><a href="#">CONTACT US</a>
  </nav>

  <section class="hero">
    <div class="hero-visual" role="img" aria-label="Smoking broken laptop photograph"></div>
    <p class="hero-tagline">Need a fast reliable company to repair your hardware?</p>
    <span class="hero-arrow prev"><svg width="10" height="10" viewBox="0 0 10 10"><path d="M7 1 3 5l4 4" stroke="#fff" stroke-width="2" fill="none"/></svg></span>
    <span class="hero-arrow next"><svg width="10" height="10" viewBox="0 0 10 10"><path d="M3 1l4 4-4 4" stroke="#fff" stroke-width="2" fill="none"/></svg></span>
  </section>

  <section class="about">
    <div class="about-head"><h2 class="section-title">ABOUT US</h2></div>
    <div class="about-body">Lorem ipsum dolor sit amet, consectetur adipiscing elit. Aliquam eget ex et arcu bibendum egestas nec a felis. Etiam vel dolor lorem. Phasellus sed pharetra lorem. Suspendisse mauris metus, condimentum vel consectetur id, consectetur nec arcu. Nullam quis nibh eros. Proin tincidunt massa ac purus tempor porttitor.</div>
  </section>

  <section class="quote" role="img" aria-label="Technician repairing computer hardware photograph">
    <span class="mark open">“</span>
    <p>Our certified technicians aren't paid on commission. No premium to upgrade to products or services you don't need or want. Even the best computer will eventually breakdown, and if we leave you happy, that's when we hope you'll come back to us.</p>
    <span class="mark close">”</span>
  </section>

  <section>
    <div class="services-head"><h2 class="section-title">SERVICES</h2></div>
    <div class="services">
      <div class="service"><span class="service-icon" role="img" aria-label="Virus removal icon"></span><p>Infections can come from many places and sometimes without your knowledge. We can clean your system back to top shape and make sure your defences are ready for the future.</p></div>
      <div class="service"><span class="service-icon" role="img" aria-label="Data transfer icon"></span><p>We can make your new computer feel like an old friend. Transfer all your files, photos, bookmarks and settings so you can pick up right where you left off.</p></div>
      <div class="service"><span class="service-icon" role="img" aria-label="Repair tools icon"></span><p>Feel like your machine is slowing down? Our technicians will test each part, replace worn components and tune everything for a faster and quieter machine.</p></div>
      <div class="service"><span class="service-icon" role="img" aria-label="Data recovery icon"></span><p>Hard drive failure? Lost files? We recover documents, photos and precious records from damaged drives and explain how to keep your data safe in future.</p></div>
      <div class="service"><span class="service-icon" role="img" aria-label="Hardware upgrade icon"></span><p>A new video card to play the latest games or a faster operating system? We source quality parts, fit them and make sure everything runs the way it should.</p></div>
      <div class="service"><span class="service-icon" role="img" aria-label="Network setup icon"></span><p>Small problems shouldn't cost an arm and a leg. We set up networks, printers and backups for homes and small offices at a fair and honest price.</p></div>
      <div class="service"><span class="service-icon" role="img" aria-label="Pick up and drop off icon"></span><p>All our services come with pick up and drop off. You won't be left to set up wireless networking, cables and printers by yourself.</p></div>
      <div class="service"><span class="service-icon" role="img" aria-label="System tune-up icon"></span><p>Over time, systems can get slowed down by unnecessary files. We clear out the clutter so your computer starts quickly and stays that way.</p></div>
    </div>
  </section>

  <footer>
    <h2 class="contact-head">CONTACT US</h2>
    <div class="contact-body">
      <div>Tel: 555-010-4567</div>
      <div>Email: dan@quickbyte.com</div>
    </div>
    <div class="site-footer">Copyright 2024 QuickByte Repairs. All rights reserved.</div>
  </footer>
</div>
</body>
</html>
```